Quillbrook Health needs a new services brochure

We need a new brochure that highlights the services that we offer at our clinic. We are a multidisciplinary health clinic that focuses on injury rehabilitation and pain management. We are looking for a brochure that will highlight our primary services to our clientele and inform potential clients of what we can offer. We pride ourselves on our quality of care and our advanced treatment techniques.
Target Market(s)
young families, athletes, people interested in their health.
Industry/Entity Type
Health And Wellness
Colors
Designer to choose colors to be used in the design.
Requirements
Must have
- We would love our new brochure to be a tri-fold that has 6 pages. We would like it to have brief information about our featured services:
- - Chiropractic
- - Massage Therapy
- - Manual Osteopathic Therapy
- - Acupuncture
- - Laser Therapy
- - Radial Shockwave Therapy
- We would also like this brochure to include a brief price list and direct billing info, About Us section & Contact information.
Nice to have
- If there is space to list that we also offer other services such as : Tissue Unwind Method, Hot Stone Massage, Cupping Technique, Pembrill Method, and Kinesiology Taping that would be great. We would like to use images similar to those that are on our website (we have hi-res of all images on the website) www.quillbrookhealth.ca and colours that would fit with our logo.

```html
<!DOCTYPE html>
<html lang="en">
<head>
<meta charset="utf-8">
<title>Quillbrook Health – Services Brochure</title>
<link href="https://fonts.googleapis.com/css2?family=Cinzel:wght@400;600&family=Questrial&display=swap" rel="stylesheet">
<style>
:root{
  --navy:#0d2a5c;
  --navy-deep:#081c40;
  --blue:#2f7fd0;
  --sky:#5aa6e8;
  --heading:#123a78;
  --ink:#222;
  --muted:#444;
  --paper:#ffffff;
  --canvas:#e4e4e4;
}
*{box-sizing:border-box;margin:0;padding:0}
html,body{width:758px;height:1200px;overflow:hidden}
body{background:var(--canvas);font-family:"Questrial",Arial,sans-serif;color:var(--ink);position:relative}
.spread{position:absolute;left:42px;width:674px;height:518px;background:var(--paper);overflow:hidden;box-shadow:0 6px 14px rgba(0,0,0,.18)}
.spread--outside{top:38px}
.spread--inside{top:628px}
.spread__bg{position:absolute;inset:0;width:674px;height:518px}
.abs{position:absolute}
.spread h1,.spread h2,.spread ul,.spread p{z-index:2}
.photo{position:absolute;border-radius:50%;border:3px solid #fff;box-shadow:0 1px 4px rgba(0,0,0,.3);z-index:1}
.serif{font-family:"Cinzel",Georgia,serif}
.small{font-size:6.6px;line-height:1.38;color:var(--muted)}
.ticks{list-style:none}
.ticks li{position:relative;padding-left:10px}
.ticks li::before{content:"";position:absolute;left:1px;top:1px;width:3px;height:5px;border:solid var(--blue);border-width:0 1.4px 1.4px 0;transform:rotate(40deg)}
.dots{list-style:none;font-size:6.8px;line-height:1.36;color:var(--muted);white-space:nowrap}
.dots li::before{content:"• ";color:var(--blue)}
.web-pill{position:absolute;bottom:12px;width:88px;height:12px;border:1px solid rgba(255,255,255,.8);border-radius:7px;color:#fff;font-size:6.4px;text-align:center;line-height:10px}
.brand{font-family:"Questrial",Arial,sans-serif;color:var(--heading);display:flex;align-items:center;gap:5px;white-space:nowrap}
.brand__dot{border-radius:50%;background:var(--blue);flex:none}
/* outside */
.about-title{left:36px;top:150px;font-size:26px;color:#111}
.about-sub{left:34px;top:181px;font-size:16.5px;color:var(--heading);letter-spacing:.3px}
.about-body{left:14px;top:206px;width:200px;text-align:justify}
.offer-badge{left:15px;top:299px;width:194px;height:54px;border-radius:14px;background:linear-gradient(#2f6fc0,#123d82);border:2px solid #fff;box-shadow:0 0 0 2px #1f5aa8;color:#fff;text-align:center}
.offer-badge__top{font-size:15px;letter-spacing:4px;padding-top:5px}
.offer-badge__main{font-size:26px;font-weight:600;line-height:1;letter-spacing:1px}
.services{left:38px;top:379px;font-size:10.2px;line-height:1.32;color:#222}
.services li{padding-left:14px}
.services li::before{width:4px;height:7px;top:2px}
.billing-pill{left:260px;top:34px;width:148px;height:16px;border-radius:8px;background:linear-gradient(#3a86d4,#14418a);color:#fff;font-size:11px;text-align:center;line-height:16px;letter-spacing:.5px}
.billing-lead{left:239px;top:67px;width:200px;font-size:7.1px;line-height:1.4;color:#111;font-weight:bold}
.billing-body{left:239px;top:111px;width:200px;text-align:justify}
.billing-list-intro{left:239px;top:196px;width:200px}
.insurers{top:219px;font-size:6.8px;line-height:1.35;color:var(--muted)}
.insurers--a{left:239px}
.insurers--b{left:356px}
.pin{left:329px;top:350px}
.address{left:239px;top:367px;width:200px;text-align:center;font-size:6.8px;line-height:1.35;color:#222}
.phone-mid{left:239px;top:395px;width:200px;text-align:center;font-size:19px;color:var(--heading)}
.social{left:318px;top:423px;display:flex;gap:6px}
.social span{width:12px;height:12px;border-radius:50%;background:var(--heading)}
.slogan{left:455px;width:205px;text-align:right;color:#fff}
.slogan--a{top:411px;font-size:21px}
.slogan--b{top:432px;font-size:32px;line-height:1}
.slogan--b em{font-style:normal;color:var(--sky)}
.slogan--c{top:461px;font-size:18px;font-family:"Questrial",Arial,sans-serif}
/* inside */
.h-chiro{left:22px;top:158px;font-size:23px;color:var(--heading)}
.list-chiro{left:28px;top:191px}
.h-osteo{left:10px;top:279px;color:var(--heading);line-height:1}
.h-osteo__a{font-size:13px;display:block}
.h-osteo__b{font-size:17px;display:block}
.list-osteo{top:316px}
.list-osteo--a{left:24px}
.list-osteo--b{left:114px}
.h-massage{left:238px;top:84px;width:202px;text-align:right;color:var(--heading);line-height:1}
.h-massage__a{font-size:23px;display:block}
.h-massage__b{font-size:15px;display:block}
.list-massage{left:252px;top:128px}
.h-acu{left:236px;top:224px;width:200px;text-align:center;font-size:22px;color:var(--heading)}
.list-acu{left:252px;top:258px}
.h-laser{left:470px;top:20px;font-size:21px;color:var(--heading)}
.list-laser{left:470px;top:48px}
.h-shock{left:456px;top:143px;width:206px;text-align:right;color:var(--heading);line-height:1.05}
.h-shock__a{font-size:17.5px;display:block}
.h-shock__b{font-size:15px;display:block}
.list-shock{left:470px;top:186px}
.contact{left:470px;top:424px;width:190px;text-align:right;color:#fff;z-index:2}
.contact__call{font-size:9px;font-weight:bold;margin-top:12px}
.contact__phone{font-size:20px;line-height:1.1}
.contact__web{font-size:7px}
</style>
</head>
<body>

<section class="spread spread--outside" aria-label="Brochure outside">
  <svg class="spread__bg" viewBox="0 0 674 518" aria-hidden="true">
    <defs>
      <linearGradient id="navyFade" x1="0" y1="0" x2="0" y2="1">
        <stop offset="0" stop-color="#0d2a5c"/><stop offset="1" stop-color="#081c40"/>
      </linearGradient>
      <linearGradient id="foldShade" x1="0" y1="0" x2="1" y2="0">
        <stop offset="0" stop-color="#000" stop-opacity=".06"/><stop offset=".1" stop-color="#000" stop-opacity="0"/>
      </linearGradient>
    </defs>
    <path d="M0,0 H262 Q120,38 0,200 Z" fill="#3a86d4"/>
    <path d="M0,0 H250 Q110,36 0,186 Z" fill="url(#navyFade)"/>
    <path d="M225,0 H449 V60 Q330,10 225,24 Z" fill="#0d2a5c" opacity=".08"/>
    <path d="M0,452 C160,478 320,500 449,466 C540,440 620,392 674,320 V518 H0 Z" fill="#3a86d4"/>
    <path d="M0,464 C160,490 320,512 449,480 C540,456 620,410 674,340 V518 H0 Z" fill="url(#navyFade)"/>
    <rect x="224.5" y="0" width="225" height="518" fill="url(#foldShade)"/>
    <rect x="449" y="0" width="225" height="518" fill="url(#foldShade)"/>
  </svg>

  <div class="photo" role="img" aria-label="Clinic reception desk and waiting area" style="left:84px;top:21px;width:110px;height:110px;background:linear-gradient(135deg,#cdbfae,#8e7a66 55%,#e8e1d6)"></div>

  <h1 class="abs about-title serif">About</h1>
  <p class="abs about-sub serif">QUILLBROOKHEALTH</p>
  <p class="abs about-body small">Quillbrook Health is a Chiropractic, Massage Therapy, Manual Osteopathy, Acupuncture, Shockwave and Laser Therapy clinic in NW Larkmoor. We bring a comprehensive approach to pain relief and injury recovery to help you get back to enjoying a healthy, active life. Our mission is to provide the best rehabilitative solutions to our patients so they can feel better in the most efficient and comfortable way possible.</p>

  <div class="abs offer-badge serif">
    <div class="offer-badge__top">SERVICES</div>
    <div class="offer-badge__main">OFFER</div>
  </div>
  <ul class="abs ticks services">
    <li>Tissue Unwind Method</li>
    <li>Hot Stone Massage</li>
    <li>Cupping Technique</li>
    <li>Pembrill Method</li>
    <li>Kinesiology</li>
  </ul>
  <div class="web-pill" style="left:68px">www.quillbrookhealth.ca</div>

  <div class="abs billing-pill serif">BILLING PROCESS</div>
  <p class="abs billing-lead">We are happy to offer direct billing to extended healthcare plans which allow direct billing and online claim submissions from providers.</p>
  <p class="abs billing-body small">As all insurance companies and plans are different, we recommend asking your plan provider directly if they allow online direct billing on your specific plan. Unfortunately at this time, insurance companies do not allow an option for direct billing for Manual Osteopathy, except in the case of Evergreen Shield and Prairie Shield. Most insurance plans do allow patients to submit manual osteopathy claims online and if you are set up for direct deposit, most plans will deposit claim payments within 48 hours.</p>
  <p class="abs billing-list-intro small">The following insurance companies typically allow online direct billing:</p>
  <ul class="abs ticks insurers insurers--a">
    <li>Prairie Shield Plan</li><li>Guild of Commerce</li><li>Cortlan</li><li>Maisonvert</li><li>Great Plains Life</li><li>Evergreen Shield</li><li>Northbay Financial Group</li>
  </ul>
  <ul class="abs ticks insurers insurers--b">
    <li>Halvorsen</li><li>Halvorsen Group</li><li>Meridalife</li><li>Maxwell Benefit</li><li>Steadfast Life</li><li>Sunridge</li>
  </ul>

  <div class="abs brand" style="left:272px;top:318px;font-size:17px"><span class="brand__dot" style="width:12px;height:12px"></span>Quillbrook Health</div>

  <svg class="abs pin" width="12" height="14" viewBox="0 0 12 14" aria-hidden="true"><path d="M6,0 C2.7,0 0,2.6 0,5.8 C0,9.8 6,14 6,14 S12,9.8 12,5.8 C12,2.6 9.3,0 6,0 Z" fill="#123a78"/><circle cx="6" cy="5.6" r="2.2" fill="#fff"/></svg>
  <p class="abs address">4410 - 1180 Larkmoor Valley Parkway NW,<br>Larkmoor, AB T0X 1K4, Canada</p>
  <p class="abs phone-mid">(555) 014-2290</p>
  <div class="abs social" aria-hidden="true"><span></span><span></span></div>
  <div class="web-pill" style="left:293px">www.quillbrookhealth.ca</div>

  <div class="abs brand" style="left:474px;top:38px;font-size:22px"><span class="brand__dot" style="width:16px;height:16px"></span>Quillbrook Health</div>
  <div class="abs" role="img" aria-label="Smiling family of four stacked together on a white bed" style="left:449px;top:92px;width:225px;height:380px;background:linear-gradient(160deg,#f2ece6,#c9a58a 45%,#6d4a36 75%,#e9e4df);clip-path:path('M0,0 H225 V228 C180,290 110,334 0,362 Z')"></div>
  <p class="abs slogan slogan--a serif">Live Life</p>
  <p class="abs slogan slogan--b serif"><em>Pain</em> Free</p>
  <p class="abs slogan slogan--c">(555) 014-2290</p>
  <div class="web-pill" style="left:518px">www.quillbrookhealth.ca</div>
</section>

<section class="spread spread--inside" aria-label="Brochure inside">
  <svg class="spread__bg" viewBox="0 0 674 518" aria-hidden="true">
    <defs>
      <linearGradient id="navyFade2" x1="0" y1="0" x2="0" y2="1">
        <stop offset="0" stop-color="#0d2a5c"/><stop offset="1" stop-color="#081c40"/>
      </linearGradient>
      <linearGradient id="foldShade2" x1="0" y1="0" x2="1" y2="0">
        <stop offset="0" stop-color="#000" stop-opacity=".06"/><stop offset=".1" stop-color="#000" stop-opacity="0"/>
      </linearGradient>
    </defs>
    <path d="M0,0 H449 V6 C360,40 300,80 224,100 C140,122 60,112 0,96 Z" fill="#3a86d4"/>
    <path d="M0,0 H449 C360,30 300,70 224,90 C140,112 60,102 0,86 Z" fill="url(#navyFade2)"/>
    <path d="M0,470 C80,460 170,420 224,380 V518 H0 Z" fill="#3a86d4"/>
    <rect x="224.5" y="0" width="225" height="518" fill="url(#foldShade2)"/>
    <rect x="449" y="0" width="225" height="518" fill="url(#foldShade2)"/>
  </svg>

  <div class="photo" role="img" aria-label="Chiropractor adjusting a patient's back" style="left:27px;top:34px;width:94px;height:94px;background:linear-gradient(150deg,#e9e4de,#6b4b45 55%,#2b2222)"></div>
  <div class="photo" role="img" aria-label="Practitioner gently treating a baby" style="left:133px;top:53px;width:90px;height:90px;background:linear-gradient(150deg,#eee,#c4a893 50%,#303030)"></div>

  <h2 class="abs h-chiro serif">Chiropractic</h2>
  <ul class="abs dots list-chiro">
    <li>Find relief from pain</li><li>Find relief from headaches</li><li>Improve movement of your back,neck and shoulders</li><li>Improve posture</li><li>Correct foot or gait problems</li><li>Correct or improve TMJ (jaw) dysfunction</li><li>Improve athletic performance</li><li>Increase energy level</li>
  </ul>
  <h2 class="abs h-osteo serif"><span class="h-osteo__a">Manual</span><span class="h-osteo__b">Osteopathic Therapy</span></h2>
  <ul class="abs dots list-osteo list-osteo--a">
    <li>Pain</li><li>Joint stiffness</li><li>Sprains</li><li>Planter Facitis</li><li>Rotator Cuff injuries</li><li>Whiplash/ MVA injuries</li>
  </ul>
  <ul class="abs dots list-osteo list-osteo--b">
    <li>Back injuries/ pain</li><li>Fibromyalgia</li><li>Headaches</li><li>Muscle injuries</li><li>Ligament tears/ injuries</li><li>Jaw pain/ TMJ disfunction</li>
  </ul>
  <div class="abs" role="img" aria-label="Therapist treating a patient's knee" style="left:0;top:374px;width:224px;height:144px;background:linear-gradient(160deg,#f4f1ee,#d6a98c 50%,#b98466);clip-path:path('M0,0 H224 V6 C170,46 80,92 0,96 Z')"></div>

  <div class="photo" role="img" aria-label="Hands massaging a client's shoulder" style="left:349px;top:8px;width:66px;height:66px;background:linear-gradient(140deg,#f2e8e0,#d4a585 50%,#8a5a40)"></div>
  <h2 class="abs h-massage serif"><span class="h-massage__a">Massage</span><span class="h-massage__b">Therapy</span></h2>
  <ul class="abs dots list-massage">
    <li>Eliminate pain</li><li>Increase range of motion</li><li>Relax tight muscles</li><li>Decrease headaches</li><li>Correct or improve TMJ (jaw) dysfunction</li><li>Decrease anxiety</li><li>Recover from injuries faster</li><li>Improve posture</li><li>Assist GI function</li>
  </ul>
  <h2 class="abs h-acu serif">Acupuncture</h2>
  <ul class="abs dots list-acu">
    <li>Find relief from pain</li><li>Increase energy levels</li><li>Improve overall mood</li><li>Improve bodily functions</li><li>Achieve body homeostasis (internal balance)</li>
  </ul>
  <div class="abs" role="img" aria-label="Clinic practitioner portrait" style="left:243px;top:362px;width:80px;height:156px;background:linear-gradient(180deg,#f1eeea,#c9b2a4 40%,#1d1d1d 70%)"></div>

  <div class="abs" role="img" aria-label="Shockwave applicator used on a patient's shoulder" style="left:449px;top:266px;width:225px;height:130px;background:linear-gradient(180deg,#ffffff 0%,#b0b0b0 35%,#3a3a3a 75%,#6a5a50);clip-path:path('M0,0 H225 V112 C150,104 71,108 0,126 Z')"></div>
  <svg class="abs" style="left:449px;top:370px;z-index:1" width="225" height="148" viewBox="0 0 225 148" aria-hidden="true">
    <path d="M0,26 C71,8 150,4 225,12 V148 H0 Z" fill="#3a86d4"/>
    <path d="M0,36 C71,18 150,14 225,22 V148 H0 Z" fill="#0d2a5c"/>
  </svg>

  <div class="photo" role="img" aria-label="Infant receiving gentle treatment" style="left:318px;top:326px;width:104px;height:104px;background:linear-gradient(150deg,#1e1e1e,#cdb3a0 50%,#f0ece8)"></div>
  <div class="photo" role="img" aria-label="Acupuncture needles placed in skin" style="left:420px;top:300px;width:100px;height:100px;background:linear-gradient(150deg,#e9d3c3,#a97a5e 50%,#5a3a2a)"></div>
  <div class="photo" role="img" aria-label="Handheld laser therapy device" style="left:378px;top:412px;width:110px;height:110px;background:linear-gradient(140deg,#0c3b7a,#3d8ee0 50%,#d9e9f8)"></div>

  <h2 class="abs h-laser serif">Laser Therapy</h2>
  <ul class="abs dots list-laser">
    <li>Post Surgical Incisions</li><li>Wound Healing</li><li>Sprains and Strains</li><li>Arthritis</li><li>Inflammation</li><li>Chronic Pain</li><li>Skin Conditions (psoriasis, cold sores, etc.)</li><li>Shin Splints</li><li>Tendonitis</li>
  </ul>
  <h2 class="abs h-shock serif"><span class="h-shock__a">Radial Shockwave</span><span class="h-shock__b">Therapy</span></h2>
  <ul class="abs dots list-shock">
    <li>Plantar Fasciitis and Heel Spurs</li><li>Patella Tendonitis (runners knee)</li><li>Tennis/ Golfer's Elbow</li><li>Chronic Shoulder Pain</li><li>Neck Pain</li><li>Shin Splints</li><li>Chronic Hip Pain</li><li>Decreased Range of Motion</li>
  </ul>

  <div class="contact abs">
    <div class="brand" style="justify-content:flex-end;color:#fff;font-size:15px"><span class="brand__dot" style="width:11px;height:11px;background:#5aa6e8"></span>Quillbrook Health</div>
    <p class="contact__call">CALL US NOW:</p>
    <p class="contact__phone">(555) 014-2290</p>
    <p class="contact__web">www.quillbrookhealth.ca</p>
  </div>
</section>

</body>
</html>
```